UK vitamin company needs a packaging label design for new vitamin range

We have a logo, and we have the product. We now need some beautiful labels to go on the boxes which bring the product range to life.
We have 7 categories: Joint Care, Heart Heath, Brain Function, Immune System, Skin, Antioxidants and Probiotics. Each of these categories should have its own look within the plumble tonic range. This can be quite subtle, but needs to be clearly visible and should be linked to the category e.g. 'Heart Health' might have a heart etc.
I have uploaded the logo, an example of the pack shape, and the sizing info for the label.
We are a fun brand, so please have some fun with this. We want the labels to be bold, and differentiated from the rest of the category.
Thanks
All images used must be 'rights free'. Many thanks
UK
It Company

```html
<!DOCTYPE html>
<html lang="en">
<head>
<meta charset="utf-8">
<title>plumble tonic – Heart Health label</title>
<link rel="stylesheet" href="https://fonts.googleapis.com/css2?family=Arimo:wght@400;700&display=swap">
<style>
  :root {
    --page: #f1f1f1;
    --label: #ffffff;
    --orange: #e0761f;
    --ink: #4b4b4b;
    --ink-soft: #6a6a6a;
    --rule: #c9c9c9;
    --swoosh: #e4e4e4;
    --yellow: #f2b51b;
    --yellow-light: #f8cf4a;
    --white: #ffffff;
  }
  * { margin: 0; padding: 0; box-sizing: border-box; }
  html, body { width: 1200px; height: 1200px; overflow: hidden; background: var(--page); }
  body { font-family: "Arimo", Arial, sans-serif; }

  .canvas { position: relative; width: 1200px; height: 1200px; }

  .label {
    position: absolute; left: 100px; top: 180px;
    width: 1000px; height: 840px;
    background: var(--label);
    overflow: hidden;
    box-shadow: 0 2px 14px rgba(0,0,0,0.08);
  }

  .brand {
    position: absolute; left: 0; right: 0; top: 60px;
    text-align: center;
    display: flex; justify-content: center; align-items: center; gap: 16px;
  }
  .brand-dot { width: 22px; height: 22px; border-radius: 50%; background: var(--orange); }
  .brand-name { font-size: 64px; font-weight: 400; color: var(--orange); letter-spacing: 1px; }

  .product-title {
    position: absolute; left: 0; right: 0; top: 200px;
    text-align: center;
    font-size: 112px; font-weight: 700; letter-spacing: -1px;
  }
  .product-title .word-heart { color: var(--ink); }
  .product-title .word-health { color: var(--orange); }

  .decor { position: absolute; inset: 0; width: 1000px; height: 840px; }

  .claim {
    position: absolute; left: 250px; top: 346px;
    font-size: 35px; line-height: 1.22; color: var(--ink);
  }

  .blurb {
    position: absolute; left: 120px; top: 500px;
    font-size: 31px; line-height: 1.2; color: var(--ink-soft);
  }

  .supplement {
    position: absolute; left: 130px; top: 670px;
    font-size: 34px; line-height: 1.15; color: var(--white);
  }
  .count {
    position: absolute; left: 610px; top: 700px;
    font-size: 34px; color: var(--ink);
  }
</style>
</head>
<body>
<div class="canvas">
  <section class="label">
    <svg class="decor" viewBox="0 0 1000 840" aria-hidden="true">
      <defs>
        <linearGradient id="band-fill" x1="0" y1="0" x2="1" y2="0">
          <stop offset="0" stop-color="var(--yellow-light)"/>
          <stop offset="1" stop-color="var(--yellow)"/>
        </linearGradient>
      </defs>
      <!-- claim rules -->
      <line x1="240" y1="335" x2="720" y2="335" stroke="var(--rule)" stroke-width="2"/>
      <path d="M240 442 L640 442 Q700 442 730 430" fill="none" stroke="var(--rule)" stroke-width="2"/>
      <!-- heart outline -->
      <path d="M790 600 C740 560 680 520 680 470 C680 420 740 400 775 440 C785 400 860 390 880 440 C900 500 830 560 790 600 Z"
            fill="none" stroke="var(--orange)" stroke-width="9" stroke-linejoin="round"/>
      <!-- grey swoosh -->
      <path d="M0 600 Q500 570 1000 520 L1000 840 L0 840 Z" fill="var(--swoosh)"/>
      <!-- yellow band -->
      <path d="M0 625 Q500 600 1000 550 L1000 840 L0 840 Z" fill="url(#band-fill)"/>
      <!-- white sweep holding the count -->
      <path d="M520 840 Q600 710 1000 650 L1000 840 Z" fill="var(--white)"/>
    </svg>

    <div class="brand">
      <span class="brand-dot"></span>
      <span class="brand-name">plumble tonic</span>
    </div>

    <h1 class="product-title"><span class="word-heart">Heart</span> <span class="word-health">Health</span></h1>

    <p class="claim">Helps Maintain Strong Heart<br>Muscle &amp; blood circulation</p>

    <p class="blurb">Lorem ipsum dolor sit amet<br>dolor sit amet</p>

    <p class="supplement">Dietary<br>Supplement</p>
    <p class="count">90 Capsules</p>
  </section>
</div>
</body>
</html>
```